Cat-products company needs smart, yet endearing, business card

We need a business card design for a new, but up-and-running, business based in Honolulu, Hawaii. The business is Purrlane Nest Co. Our first product is the most environmentally-friendly cat grass kit ever seen on the planet. Future products, currently in the R&D phase, will include a variety of exciting cat scratchers. We also do consulting work to help apartment-dwellers make their home more cat-friendly and, in the future, plan on doing full, custom installs of structure to create high walkways for cats.

Target Market(s)

Middle-aged, apartment-dwelling, middle-class workers who own 1 or more cats and who dote on them.

Industry/Entity Type

Pet Care

Contact Information for Business Card

A striking, professional, yet warm and friendly design is what we're after.

Font styles to use
Serif
Sans Serif
Other font styles liked:
• Comfortaa

Colors

Designer to choose colors to be used in the design.

Requirements
Must have
• The company logo: (see attachment)
• The company name: Purrlane Nest Co
• The web address: www.purrlanenestco.example
• Email: support@purrlanenestco.example
• Phone: +1 (808) 555 0172
• Update (Fri Jun 30 3017 7:45pm Hawaii Time) I would like, is possible, uploaded picture of the cat grass kit on the back of the card with some text along the lines of: Purrlane Nest Co - Where The Freshest Kitty Sprouts Begin
Nice to have
• A cat picture, cartoon, real or silhouette that illustrates cats in action and/or relaxing; ie using the apartment space to live, play and relax in and being well-contented.
• Most of the website is done in the font: Comfortaa. It might be nice to continue using this for brand consistency.
Should not have
• Hard-to-read fonts.

```html
<!DOCTYPE html>
<html lang="en">
<head>
<meta charset="utf-8">
<title>Purrlane Nest Co — Business Card</title>
<link rel="stylesheet" href="https://fonts.googleapis.com/css2?family=Jost:wght@400;500;600;700&display=swap">
<style>
  :root {
    --backdrop: #1d1d1f;
    --card: #ffffff;
    --amber: #f4aa1e;
    --cocoa: #5b3b34;
    --ink: #2f2f2f;
    --muted: #555555;
    --rule: #6a6a6a;
  }
  * { box-sizing: border-box; margin: 0; padding: 0; }
  html, body {
    width: 1200px; height: 1000px; overflow: hidden;
    background: var(--backdrop);
    font-family: "Jost", "Futura", sans-serif;
  }
  .canvas { position: relative; width: 1200px; height: 1000px; }

  .card {
    position: absolute; left: 250px; width: 700px; height: 400px;
    background: var(--card); border-radius: 34px; overflow: hidden;
    box-shadow: 0 18px 40px rgba(0,0,0,.45);
  }
  .card--front { top: 60px; }
  .card--back { top: 540px; }

  .wordmark {
    display: flex; align-items: center; gap: 14px;
    color: var(--amber); font-weight: 700; letter-spacing: .5px;
  }
  .wordmark__square { width: 30px; height: 30px; background: var(--cocoa); border-radius: 4px; }
  .card--front .wordmark {
    position: absolute; left: 50%; top: 50%; transform: translate(-50%, -50%);
    font-size: 44px; white-space: nowrap;
  }
  .card--back .wordmark {
    position: absolute; left: 50px; top: 130px; font-size: 30px; white-space: nowrap;
  }
  .card--back .wordmark__square { width: 24px; height: 24px; }

  .accent-tab {
    position: absolute; right: 0; top: 60px; width: 12px; height: 50px;
    background: var(--amber); border-radius: 6px 0 0 6px;
  }
  .person { position: absolute; right: 60px; top: 62px; text-align: right; }
  .person__name { color: var(--amber); font-size: 24px; font-weight: 600; letter-spacing: 1px; }
  .person__role { color: var(--muted); font-size: 15px; margin-top: 2px; }
  .rule-top {
    position: absolute; left: 330px; right: 170px; top: 100px;
    border-top: 1.5px solid var(--rule);
  }
  .address {
    position: absolute; right: 60px; top: 150px; text-align: right;
    color: var(--ink); font-size: 15px; line-height: 1.45;
  }
  .rule-bottom {
    position: absolute; left: 140px; right: 250px; top: 262px;
    border-top: 1.5px solid var(--rule);
  }
  .contacts {
    position: absolute; left: 140px; top: 282px; list-style: none;
    color: var(--ink); font-size: 16px; line-height: 1.55;
  }
  .contacts li { display: flex; align-items: center; gap: 12px; }
  .contacts svg { width: 13px; height: 13px; fill: var(--amber); flex: none; }
  .contacts .highlight { color: var(--amber); }
</style>
</head>
<body>
<main class="canvas">
  <section class="card card--front" aria-label="Card front">
    <div class="wordmark"><span class="wordmark__square"></span>Purrlane Nest Co</div>
  </section>

  <section class="card card--back" aria-label="Card back">
    <span class="accent-tab"></span>
    <div class="wordmark"><span class="wordmark__square"></span>Purrlane Nest Co</div>

    <div class="person">
      <p class="person__name">LENA KAHALE</p>
      <p class="person__role">Director</p>
    </div>
    <div class="rule-top"></div>

    <p class="address">Your Street Address,<br>Honolulu,9681</p>

    <div class="rule-bottom"></div>
    <ul class="contacts">
      <li>
        <svg viewBox="0 0 24 24" aria-hidden="true"><path d="M6.6 10.8a15.5 15.5 0 0 0 6.6 6.6l2.2-2.2c.3-.3.7-.4 1-.2 1.1.4 2.3.6 3.6.6.6 0 1 .4 1 1V20c0 .6-.4 1-1 1C10.6 21 3 13.4 3 4c0-.6.4-1 1-1h3.5c.6 0 1 .4 1 1 0 1.3.2 2.5.6 3.6.1.3 0 .7-.2 1z"/></svg>
        +1 (808) 555 0172
      </li>
      <li>
        <svg viewBox="0 0 24 24" aria-hidden="true"><path d="M2 5h20v14H2zm2 2v.5l8 5 8-5V7l-8 5z"/></svg>
        support@purrlanenestco.example
      </li>
      <li>
        <svg viewBox="0 0 24 24" aria-hidden="true"><circle cx="12" cy="12" r="10"/></svg>
        <span>www.<span class="highlight">purrlanenestco</span>.example</span>
      </li>
    </ul>
  </section>
</main>
</body>
</html>
```